Business Card Design Project

I need a business card design for a new business called Thornal Insurance Services. I am a small insurance broker that will provide business insurance services mostly to contractors and small businesses. My business is all about customer service and assistance rather than being a price driven/focused business. I want my business card to be professional giving the impression that I am larger than one person but not a corporate company. I have attached a copy of my logo.
Updates

Hi all

I have been advised that I need to show the following info for compliance reasons on my card. It only has to be small.

Can you please include either front or back:

Thornal Insurance Services Pty Ltd [ABN 61728405913] AR No 586027 as Authorised Representative of Carrodine Insurance Group Pty Ltd ACN 274 619 508 ABN 82 274 619 508 AFS Licence No 718246

Reason: I need a further change to be made to the design. I need the contact number of 1300584619 added to the business card.

Hi All

I need one last change made to the card.

Can you please include the phone number 1300584619 to the card. If possible can this be made fairly clear on the card, either large on the back or another design idea you may have.

Target Market(s)

30+ Professionals

Industry/Entity Type

Insurance

Requirements
Must have
• I want a double sided design. My details to go on the card are as follows:

Dean Thornal QRTMOL (Snr Assoc.) CIP
Director
PO Box 782, Fernmoor SA 5071
Phone: 0438 612 704
Fax 08 8347 2910
Email: dean@thornalcover.example.au
Website: http://www.thornalcover.example.au
Twitter: Thornalcover
Facebook: facebook.com/thornalcover

```html
<!DOCTYPE html>
<html lang="en">
<head>
<meta charset="utf-8">
<title>Thornal Insurance Services – Business Card</title>
<link rel="stylesheet" href="https://fonts.googleapis.com/css2?family=Roboto+Condensed:wght@400;700&display=swap">
<style>
  :root {
    --page: #3a3a3a;
    --card-white: #ffffff;
    --card-grey: #bcbdc0;
    --ink: #231f20;
    --text-grey: #4a4a4a;
    --brand-red: #e31b23;
    --white: #ffffff;
  }
  * { box-sizing: border-box; margin: 0; padding: 0; }
  html, body { width: 1200px; height: 1200px; overflow: hidden; }
  body {
    background: var(--page);
    font-family: "Roboto Condensed", Arial, sans-serif;
    position: relative;
  }
  .card {
    position: absolute;
    left: 150px;
    width: 900px;
    height: 515px;
    overflow: hidden;
  }
  .card--front { top: 55px; background: var(--card-white); }
  .card--back { top: 630px; background: var(--card-grey); }

  .swoosh { position: absolute; inset: 0; width: 900px; height: 515px; }

  /* brand name set in the card's text font with one plain circle beside it */
  .brand-name {
    position: absolute;
    display: flex;
    align-items: center;
    gap: 14px;
    font-family: "Roboto Condensed", Arial, sans-serif;
    font-weight: 700;
    color: var(--ink);
    white-space: nowrap;
  }
  .brand-name__dot {
    flex: none;
    width: 26px; height: 26px; border-radius: 50%;
    background: var(--brand-red);
  }
  .card--front .brand-name { left: 70px; top: 210px; width: 300px; justify-content: center; font-size: 60px; }
  .card--back .brand-name { left: 0; right: 0; top: 65px; justify-content: center; font-size: 54px; }
  .card--back .brand-name__dot { width: 22px; height: 22px; }

  .holder {
    position: absolute; right: 130px; top: 100px; text-align: right;
    color: var(--ink); font-size: 22px; line-height: 1.15;
  }
  .holder__post { font-size: 17px; color: var(--text-grey); }
  .holder__title { display: block; font-size: 19px; color: var(--text-grey); }

  .company {
    font-family: "Roboto Condensed", Arial, sans-serif;
    font-weight: 700; color: var(--ink);
    white-space: nowrap;
  }
  .card--front .company { position: absolute; right: 110px; top: 180px; font-size: 40px; }

  .contacts {
    position: absolute; right: 60px; top: 265px;
    list-style: none; text-align: right;
    color: var(--text-grey); font-size: 20px; line-height: 27px;
  }
  .contacts li { display: flex; justify-content: flex-end; align-items: center; gap: 12px; }
  .contacts .icon { width: 18px; height: 18px; flex: none; }
  .contacts .icon--blank { visibility: hidden; }
  .contacts .web { color: var(--ink); }

  .band {
    position: absolute; left: 0; right: 0; top: 190px; height: 115px;
    background: var(--white);
    display: flex; align-items: center; justify-content: center;
  }
  .card--back .company { font-size: 56px; }

  .compliance {
    position: absolute; left: 0; right: 0; top: 330px;
    text-align: center; color: var(--white); font-size: 17px; line-height: 23px;
  }
  .compliance__entity { font-weight: 700; font-size: 19px; }
  .compliance__web { font-size: 20px; margin-top: 4px; }
</style>
</head>
<body>

<section class="card card--front" aria-label="Business card front">
  <svg class="swoosh" viewBox="0 0 900 515" aria-hidden="true">
    <path d="M415 0 C 320 170, 350 420, 590 515 L 545 515 C 345 430, 330 200, 415 0 Z" fill="var(--brand-red)"/>
  </svg>

  <div class="brand-name">
    <span class="brand-name__dot"></span>
    <span>Thornal</span>
  </div>

  <p class="holder">
    Dean Thornal QRTMOL <span class="holder__post">(Snr Assoc.) CIP</span>
    <span class="holder__title">Director</span>
  </p>

  <p class="company">Thornal Insurance</p>

  <ul class="contacts">
    <li>0438 612 704
      <svg class="icon" viewBox="0 0 18 18"><circle cx="9" cy="9" r="8" fill="none" stroke="var(--brand-red)" stroke-width="1.5"/><path d="M6 5 l2 0 l1 2.5 l-1.3 1 a6 6 0 0 0 2.8 2.8 l1-1.3 l2.5 1 l0 2 c-4 0.5 -8.5 -4 -8 -8z" fill="var(--brand-red)"/></svg>
    </li>
    <li>1 300 584619
      <svg class="icon icon--blank" viewBox="0 0 18 18"></svg>
    </li>
    <li>08 8347 2910
      <svg class="icon" viewBox="0 0 18 18"><rect x="4" y="1.5" width="10" height="6" fill="none" stroke="var(--brand-red)" stroke-width="1.4"/><rect x="1.5" y="7.5" width="15" height="6" fill="none" stroke="var(--brand-red)" stroke-width="1.4"/><rect x="4" y="12" width="10" height="4.5" fill="none" stroke="var(--brand-red)" stroke-width="1.4"/></svg>
    </li>
    <li>dean@thornalcover.example.au
      <svg class="icon" viewBox="0 0 18 18"><rect x="1.5" y="4" width="15" height="10" fill="none" stroke="var(--brand-red)" stroke-width="1.4"/><path d="M1.5 4 L9 10 L16.5 4" fill="none" stroke="var(--brand-red)" stroke-width="1.4"/></svg>
    </li>
    <li>Thornalcover
      <svg class="icon" viewBox="0 0 18 18"><rect x="1" y="1" width="16" height="16" rx="3" fill="var(--brand-red)"/></svg>
    </li>
    <li>thornalcover
      <svg class="icon" viewBox="0 0 18 18"><rect x="1" y="1" width="16" height="16" fill="var(--brand-red)"/></svg>
    </li>
    <li class="web">www.thornalcover.example.au
      <svg class="icon icon--blank" viewBox="0 0 18 18"></svg>
    </li>
  </ul>
</section>

<section class="card card--back" aria-label="Business card back">
  <div class="brand-name">
    <span class="brand-name__dot"></span>
    <span>Thornal</span>
  </div>

  <div class="band">
    <p class="company">Thornal Insurance</p>
  </div>

  <div class="compliance">
    <p class="compliance__entity">Thornal Insurance Services Pty Ltd</p>
    <p>ABN 61728405913 &nbsp;AR No 586027</p>
    <p>as Authorised Representative of Carrodine Insurance Group Pty Ltd</p>
    <p>ACN 274 619 508 &nbsp;| &nbsp;ABN 82 274 619 508 | AFS Licence No 718246</p>
    <p class="compliance__web">www.thornalcover.example.au</p>
  </div>
</section>

</body>
</html>
```